Brochure for The Riverside Lantern Club Private Venue

Brochure to sell the venue and food & beverage services for private parties
Venue name is The Riverside Lantern Club

Target Market(s)

Age: 25 - 40 female

Industry/Entity Type

Events

Requirements
Must have
• Please also put the venue name, address, website and phone
• Riverside Lantern Club
• 4718 Marigold Crest Blvd
• National City, CA 91950
• RiversideLantern.Club
• (858) 555-0193
• TONS of photos. You can grab more photos if needed on the website
Nice to have
• Festive Vibe -

```html
<!DOCTYPE html>
<html lang="en">
<head>
<meta charset="UTF-8">
<title>The Riverside Lantern Club – Private Venue Brochure</title>
<link rel="stylesheet" href="https://fonts.googleapis.com/css2?family=Cinzel:wght@700&family=Open+Sans:wght@400;600&display=swap">
<style>
  :root {
    --backdrop: #d9d8dc;
    --paper: #f7f7f7;
    --ink: #1a1a1a;
    --ink-soft: #4a4a4a;
    --gold-start: #f2c21b;
    --gold-end: #f29a1d;
    --sky-blue: #3d97d3;
    --sky-blue-dark: #2b86c6;
    --white: #ffffff;
    --photo-dark: #3a332f;
    --photo-mid: #8a6a4c;
    --photo-light: #e8e4e2;
    --photo-blush: #d9b6b4;
  }
  * { box-sizing: border-box; margin: 0; padding: 0; }
  html, body {
    width: 1200px;
    height: 840px;
    overflow: hidden;
    background: var(--backdrop);
  }
  .canvas {
    width: 1200px;
    height: 840px;
    display: flex;
    align-items: center;
    justify-content: center;
  }
  .brochure-cover {
    position: relative;
    width: 580px;
    height: 780px;
    background: var(--paper);
    box-shadow: 0 10px 30px rgba(0,0,0,0.18);
    overflow: hidden;
  }
  .venue-mark {
    position: absolute;
    top: 44px;
    left: 52px;
    display: flex;
    align-items: center;
    gap: 10px;
    font-family: "Open Sans", sans-serif;
    font-weight: 600;
    font-size: 24px;
    color: var(--ink);
    letter-spacing: 0.3px;
  }
  .venue-mark__square {
    width: 18px;
    height: 18px;
    background: var(--gold-start);
  }
  .venue-photo {
    position: absolute;
    top: 120px;
    left: 0;
    width: 580px;
    height: 350px;
    background: linear-gradient(180deg, var(--photo-dark) 0%, var(--photo-light) 30%, var(--photo-light) 48%, var(--photo-mid) 70%, var(--photo-dark) 100%);
  }
  .occasion-banner {
    position: absolute;
    top: 445px;
    left: 0;
    width: 520px;
    height: 86px;
    background: linear-gradient(90deg, var(--gold-start), var(--gold-end));
    clip-path: polygon(0 0, 100% 0, 96% 100%, 0 100%);
    padding: 14px 0 0 34px;
    font-family: "Cinzel", serif;
    font-weight: 700;
    line-height: 1.25;
    color: var(--white);
  }
  .occasion-banner__primary { font-size: 24px; }
  .occasion-banner__secondary { font-size: 20px; }
  .photo-strip {
    position: absolute;
    top: 548px;
    left: 34px;
    right: 34px;
    height: 100px;
    display: flex;
    gap: 12px;
  }
  .photo-strip__item { flex: 1; }
  .photo-strip__item--tables { background: linear-gradient(160deg, var(--photo-light), var(--photo-mid)); }
  .photo-strip__item--balloons { background: linear-gradient(160deg, var(--white), var(--photo-blush)); }
  .photo-strip__item--lights { background: linear-gradient(160deg, var(--photo-dark), var(--photo-mid)); }
  .address-band {
    position: absolute;
    left: 0;
    top: 666px;
    width: 580px;
    height: 54px;
    background: linear-gradient(90deg, var(--sky-blue), var(--sky-blue-dark));
    display: flex;
    align-items: center;
    gap: 12px;
    padding-left: 40px;
    font-family: "Open Sans", sans-serif;
    font-size: 18px;
    color: var(--white);
  }
  .address-band svg { flex: none; }
  .contact-line {
    position: absolute;
    left: 40px;
    right: 40px;
    top: 734px;
    display: flex;
    justify-content: space-between;
    font-family: "Open Sans", sans-serif;
    font-size: 16px;
    font-weight: 600;
    color: var(--ink-soft);
  }
</style>
</head>
<body>
  <main class="canvas">
    <article class="brochure-cover">
      <header class="venue-mark">
        <span class="venue-mark__square"></span>
        <span class="venue-mark__name">Riverside Lantern Club</span>
      </header>

      <div class="venue-photo" role="img" aria-label="Photo of the venue hall set for a party with long wooden tables, cross-back chairs, white balloons and string lights"></div>

      <div class="occasion-banner">
        <p class="occasion-banner__primary">Birthday Party, Baby Shower</p>
        <p class="occasion-banner__secondary">Celebration of Life, or Quincenira</p>
      </div>

      <div class="photo-strip">
        <div class="photo-strip__item photo-strip__item--tables" role="img" aria-label="Photo of a dressed banquet table with flowers"></div>
        <div class="photo-strip__item photo-strip__item--balloons" role="img" aria-label="Photo of a balloon arch and pink backdrop"></div>
        <div class="photo-strip__item photo-strip__item--lights" role="img" aria-label="Photo of string lights over the hall at evening"></div>
      </div>

      <div class="address-band">
        <svg width="20" height="24" viewBox="0 0 20 24" aria-hidden="true">
          <path d="M10 1C5 1 1.5 4.6 1.5 9.2 1.5 15 10 23 10 23s8.5-8 8.5-13.8C18.5 4.6 15 1 10 1z" fill="#ffffff"/>
          <circle cx="10" cy="9.3" r="3.3" fill="#3d97d3"/>
        </svg>
        <span class="address-band__text">4718 Marigold Crest Blvd National City, CA 91950</span>
      </div>

      <footer class="contact-line">
        <span class="contact-line__web">RiversideLantern.Club</span>
        <span class="contact-line__phone">(858) 555-0193</span>
      </footer>
    </article>
  </main>
</body>
</html>
```